Christmas Concert

"The Ashcombe Voices" is Thornwick Manor's professional chamber choir. www.ashcombevoices-example.com

They are performing a Christmas concert in Oxford's oldest building, St Aldric by the Westmarch (almost 1,000 years old), and the concert will be by candlelight.

We are looking for a dramatic and sophisticated Christmas poster that will stand out in the crowd of other posters in Oxford city centre.

We are thinking of calling the concert "Christmas with the Ashcombe Voices" or "Christmas Carols by Candlelight" but we're open to suggestions.

The poster will be used for digital dissemination (as well as Chatterly/Quipster) as well as print - A2 (portrait) will be the maximum size.

See attached photo of the ensemble. It would be a good to incorporate this in some way.
Updates

Industry/Entity Type

Building

Requirements
Nice to have
• The Ashcombe Voices
• Neil Carrow-Pritchard, Director
• Sunday 8 December
• 8pm
• Tickets £10/£5
• AshcombeVoices-example.com

```html
<!DOCTYPE html>
<html lang="en">
<head>
<meta charset="utf-8">
<title>Christmas Carols by Candlelight – The Ashcombe Voices</title>
<link rel="stylesheet" href="https://fonts.googleapis.com/css2?family=Gilda+Display&family=Ultra&display=swap">
<style>
  :root {
    --ink: #000000;
    --white: #ffffff;
    --red: #e0141b;
    --frame: #f4f4f4;
    --serif: "Gilda Display", Georgia, serif;
    --slab: "Ultra", "Rockwell", serif;
  }
  html, body { margin: 0; padding: 0; overflow: hidden; background: var(--ink); }
  .poster {
    position: relative;
    width: 849px;
    height: 1200px;
    overflow: hidden;
    background: var(--ink);
    color: var(--white);
  }
  .backdrop {
    position: absolute;
    inset: 0;
    background:
      radial-gradient(circle at 80% 70%, rgba(40,170,60,.85) 0, rgba(40,170,60,0) 28%),
      radial-gradient(circle at 92% 45%, rgba(240,200,40,.8) 0, rgba(240,200,40,0) 20%),
      radial-gradient(circle at 60% 40%, rgba(120,110,230,.75) 0, rgba(120,110,230,0) 26%),
      radial-gradient(circle at 85% 12%, rgba(230,60,160,.7) 0, rgba(230,60,160,0) 25%),
      radial-gradient(circle at 65% 88%, rgba(220,70,40,.8) 0, rgba(220,70,40,0) 22%),
      radial-gradient(circle at 40% 30%, rgba(170,60,200,.45) 0, rgba(170,60,200,0) 22%),
      linear-gradient(90deg, #000 0%, #000 22%, #3a1450 50%, #6a2a8a 75%, #2e6b2a 100%);
  }
  .presenter {
    position: absolute; top: 6px; left: 0; right: 0;
    margin: 0; text-align: center;
    font: 400 62px/1 var(--serif);
    color: var(--red);
  }
  .presents {
    position: absolute; top: 82px; left: 0; right: 0;
    margin: 0; text-align: center;
    font: 400 32px/1 var(--serif);
  }
  .title {
    position: absolute; top: 118px; left: 0; right: 0;
    margin: 0; text-align: center;
    font: 400 96px/0.93 var(--serif);
    text-shadow: 2px 2px 3px rgba(0,0,0,.6);
  }
  .details {
    position: absolute; left: 45px; top: 360px;
    font-family: var(--slab);
    text-shadow: 1px 1px 2px rgba(0,0,0,.5);
  }
  .details p { margin: 0; }
  .date { font-size: 38px; line-height: 64px; }
  .venue { font-size: 25px; line-height: 42px; margin-top: 4px !important; }
  .tickets { font-size: 20px; line-height: 32px; }
  .ensemble-photo {
    position: absolute; left: -20px; top: 606px;
    width: 565px; height: 395px;
    background: var(--frame);
    transform: rotate(-3deg);
    box-shadow: 0 6px 14px rgba(0,0,0,.6);
  }
  .ensemble-photo .image {
    position: absolute; inset: 12px;
    background: linear-gradient(180deg, #cfd9e6 0%, #c9a86e 25%, #b48a52 52%, #4d5a3a 70%, #6b2020 85%, #8f8f86 100%);
  }
  .signoff {
    position: absolute; left: 0; right: 0; top: 1050px;
    text-align: center;
    font-family: var(--slab);
    text-shadow: 1px 1px 2px rgba(0,0,0,.6);
  }
  .signoff p { margin: 0; }
  .signoff .name { font-size: 45px; line-height: 54px; }
  .signoff .director { font-size: 24px; line-height: 36px; }
  .signoff .web { font-size: 25px; line-height: 36px; }
</style>
</head>
<body>
<div class="poster">
  <div class="backdrop" role="img" aria-label="Blurred colourful Christmas lights and a decorated tree with ribbons and baubles"></div>

  <p class="presenter">The Ashcombe Voices</p>
  <p class="presents">present</p>
  <h1 class="title">Christmas Carols<br>by Candlelight</h1>

  <div class="details">
    <p class="date">Sunday 8 December</p>
    <p class="date">at 8pm</p>
    <p class="venue">St Aldric by the Westmarch</p>
    <p class="tickets">Tickets £10/£5 on the door</p>
  </div>

  <div class="ensemble-photo">
    <div class="image" role="img" aria-label="The choir in evening dress standing in the gardens in front of Thornwick Manor"></div>
  </div>

  <div class="signoff">
    <p class="name">The Ashcombe Voices</p>
    <p class="director">Neil Carrow-Pritchard, Director.</p>
    <p class="web">www.ashcombevoices-example.com</p>
  </div>
</div>
</body>
</html>
```